Business Cards used to invite people to our church

We are a church and have need of a business card sized advertisement that allows our members to hand them out in order to invite people to the church. I need the front of the card to say "You're Invited" or "Come Check us out". with the service times on the back of the card later.
I have attached one of the OLD cards we have used in the past, but we want a complete makeover, into a more modern style that does not require the image.
I am also replacing the old logo with a newer "flat" logo which is attached.
Please use marketing colors. (blue or red or something that catches attention)
Create a card that DOES NOT have the picture of the two people on the front
The information on the sample card back is correct to go onto new card
Target Market(s)
anyone
Industry/Entity Type
Business
Contact Information for Business Card
sertice times and address information which you can get from the sample card I uploaded. It should have "You're Invited" or "Come Check us out" on the front of the card with out logo.

```html
<!DOCTYPE html>
<html lang="en">
<head>
<meta charset="utf-8">
<title>Invitation Card – Front and Back</title>
<link href="https://fonts.googleapis.com/css2?family=Open+Sans:wght@400;600;700&display=swap" rel="stylesheet">
<style>
  :root {
    --page-bg: #ece9e4;
    --sky-deep: #10259a;
    --sky-mid: #2447d6;
    --sky-light: #4f74ee;
    --night: #0a1440;
    --accent-red: #e41e2b;
    --accent-red-dark: #c3121f;
    --accent-cyan: #22b8ee;
    --ink-white: #ffffff;
    --card-w: 560px;
    --card-h: 320px;
  }
  html, body {
    margin: 0;
    padding: 0;
    width: 1200px;
    height: 913px;
    overflow: hidden;
    background: var(--page-bg);
    font-family: "Open Sans", Arial, sans-serif;
  }
  .canvas {
    position: relative;
    width: 1200px;
    height: 913px;
  }
  .card {
    position: absolute;
    left: 320px;
    width: var(--card-w);
    height: var(--card-h);
    overflow: hidden;
    box-shadow: 0 10px 28px rgba(0,0,0,0.25);
  }
  .card-front { top: 110px; }
  .card-back  { top: 490px; }
  .card-art {
    position: absolute;
    inset: 0;
    width: 100%;
    height: 100%;
    display: block;
  }

  /* Front */
  .church-name {
    position: absolute;
    left: 300px;
    top: 62px;
    width: 240px;
    margin: 0;
    color: var(--ink-white);
    font-weight: 700;
    font-size: 30px;
    line-height: 1.05;
    letter-spacing: 0.5px;
    text-transform: uppercase;
  }
  .invite-line {
    position: absolute;
    left: 236px;
    top: 206px;
    margin: 0;
    font-weight: 400;
    font-size: 34px;
    letter-spacing: 0.5px;
    text-transform: uppercase;
    white-space: nowrap;
  }
  .invite-you { color: var(--accent-red); }
  .invite-word { color: var(--ink-white); }

  /* Back */
  .contact-block {
    position: absolute;
    top: 38px;
    left: 0;
    right: 0;
    text-align: center;
    color: var(--ink-white);
    font-size: 14px;
    line-height: 1.55;
    letter-spacing: 0.6px;
    text-transform: uppercase;
  }
  .contact-block p { margin: 0; }
  .service-times {
    position: absolute;
    left: 40px;
    right: 40px;
    top: 150px;
    margin: 0;
    padding: 0;
    list-style: none;
    color: var(--ink-white);
    font-size: 14px;
    letter-spacing: 0.6px;
    text-transform: uppercase;
  }
  .service-row {
    display: flex;
    align-items: baseline;
    margin-bottom: 22px;
  }
  .service-leader {
    flex: 1;
    margin: 0 6px;
    border-bottom: 2px dotted rgba(255,255,255,0.9);
    transform: translateY(-4px);
  }
</style>
</head>
<body>
<main class="canvas">

  <section class="card card-front" aria-label="Card front">
    <svg class="card-art" viewBox="0 0 560 320" xmlns="http://www.w3.org/2000/svg">
      <defs>
        <linearGradient id="skyFront" x1="0" y1="0" x2="1" y2="1">
          <stop offset="0" stop-color="var(--sky-light)"/>
          <stop offset="0.45" stop-color="var(--sky-mid)"/>
          <stop offset="0.8" stop-color="var(--sky-deep)"/>
          <stop offset="1" stop-color="var(--night)"/>
        </linearGradient>
        <linearGradient id="redPanel" x1="0" y1="0" x2="1" y2="1">
          <stop offset="0" stop-color="var(--accent-red)"/>
          <stop offset="1" stop-color="var(--accent-red-dark)"/>
        </linearGradient>
      </defs>
      <rect width="560" height="320" fill="url(#skyFront)" role="img" aria-label="Photo of a blue evening sky with clouds and a tree silhouette"/>
      <path d="M0 0 H330 C235 55 165 170 145 320 H0 Z" fill="url(#redPanel)"/>
      <path d="M330 0 C235 55 165 170 145 320" fill="none" stroke="var(--accent-cyan)" stroke-width="12"/>
      <path d="M345 0 C250 58 182 172 162 320" fill="none" stroke="var(--accent-cyan)" stroke-opacity="0.35" stroke-width="4"/>
    </svg>
    <h1 class="church-name">Cedar Hill<br>Gathering</h1>
    <p class="invite-line"><span class="invite-you">You're</span> <span class="invite-word">Invited</span></p>
  </section>

  <section class="card card-back" aria-label="Card back">
    <svg class="card-art" viewBox="0 0 560 320" xmlns="http://www.w3.org/2000/svg">
      <defs>
        <linearGradient id="skyBack" x1="0" y1="0" x2="1" y2="1">
          <stop offset="0" stop-color="var(--sky-mid)"/>
          <stop offset="0.5" stop-color="var(--sky-light)"/>
          <stop offset="0.85" stop-color="var(--sky-deep)"/>
          <stop offset="1" stop-color="var(--night)"/>
        </linearGradient>
      </defs>
      <rect width="560" height="320" fill="url(#skyBack)" role="img" aria-label="Photo of a blue evening sky with clouds and a tree silhouette"/>
    </svg>
    <div class="contact-block">
      <p>P: 1-800-555-0142</p>
      <p>www.cedarhillgathering.org</p>
      <p>A: 2480 W. Birch Lane - Fairview, TX 75099</p>
    </div>
    <ul class="service-times">
      <li class="service-row"><span>Sunday</span><span class="service-leader"></span><span>9:00 AM</span></li>
      <li class="service-row"><span>Sunday</span><span class="service-leader"></span><span>11 AM</span></li>
      <li class="service-row"><span>Wed. Bible Class</span><span class="service-leader"></span><span>7:00 PM</span></li>
    </ul>
  </section>

</main>
</body>
</html>
```